Newsletter-Design und Programmierung
Zielgruppe
Leider ist bei mir keine Anpassung der Schieberegler möglich, diese Angabe sind also NICHT korrekt.
Zielgruppe des Newsletters sind kleine und mittlere Unternehmen, Selbständige und Freiberufler. Das Design soll dementsprechend professionell und schlicht sein und außerdem das bereits existierende Design der o.g. Klickmax LP sowie der Website www.kanzlei-morvenstein.de berücksichtigen.
Aufgabenstellung
Es soll ein einfacher HTML-Newsletter nach Vorgabe designed und anschließend auch programmiert werden.
Hier noch einige Details zur technischen Umsetzung:
- nicht mehr als 600px Breite (innerhalb eines 100% Containers)
- per CSS angepasste Varianten für Smartphones und Tablets
- Außerdem sollte die Positionierung im Gegensatz zu Webseiten sicherheitshalber per Tabellen realisiert werden.
Eine Struktur-Vorlage, auf der man ein Design aufbauen lassen könnte, wäre z.B. http://quirbelgeruest.net/

```html
<!DOCTYPE html>
<html lang="de">
<head>
<meta charset="utf-8">
<title>Kanzlei Morvenstein Newsletter</title>
<link href="https://fonts.googleapis.com/css2?family=Arimo:ital,wght@0,400;0,700;1,400&display=swap" rel="stylesheet">
<style>
:root{
  --page:#efefef;
  --card:#ffffff;
  --text:#8a8a8a;
  --dark:#222222;
  --red:#c8111d;
  --red-bright:#e1141f;
  --rule:#e2e2e2;
}
*{box-sizing:border-box;margin:0;padding:0}
html,body{width:1200px;height:3434px;overflow:hidden}
body{background:var(--page);font-family:"Arimo",Arial,sans-serif;color:var(--text);font-size:23px;line-height:1.72;position:relative}
.abs{position:absolute}
.preheader{left:2px;top:14px;width:1196px;font-size:23px;line-height:1.6;color:#8d8d8d}
.brand{left:36px;top:172px;display:flex;align-items:center;gap:18px}
.brand-dot{width:80px;height:80px;border-radius:50%;background:var(--red)}
.brand-name{font-size:40px;line-height:1.05;color:var(--dark)}
.hero{left:0;top:312px;width:1200px;height:498px;background:var(--card)}
.hero-visual{left:0;top:0;width:790px;height:424px;background:linear-gradient(100deg,#ffffff 10%,#d9d9d9 45%,#f4f4f4 60%,#c21a22 78%,#ffffff 95%)}
.hero-tag{left:28px;top:318px;font-size:24px;color:#111}
.hero-claim{left:26px;top:352px;font-size:32px;color:var(--red)}
.hero-strip{left:0;top:424px;width:790px;height:70px;background:var(--red);display:flex;align-items:center;padding-left:22px;gap:20px;color:#fff;font-size:35px;font-style:italic}
.hero-side{left:832px;top:34px;width:360px}
.hero-title{font-size:35px;line-height:1.52;color:var(--dark)}
.hero-sub{margin-top:18px;font-size:23px;line-height:1.72}
.hero-sub b{color:#8a8a8a}
.cta{display:inline-block;margin-top:30px;background:var(--red-bright);color:#fff;font-weight:700;font-size:22px;padding:8px 60px 8px 16px;border-radius:4px;position:relative}
.cta svg{position:absolute;right:10px;top:10px}
.card{background:var(--card);border-radius:8px;box-shadow:0 4px 8px rgba(0,0,0,.05);padding:36px 40px}
.card h2{font-weight:400;font-size:29px;color:var(--dark);margin-bottom:26px}
.c1{left:4px;top:853px;width:748px;height:673px}
.c2{left:4px;top:1565px;width:748px;height:565px}
.c3{left:4px;top:2171px;width:748px;height:226px;padding-top:26px}
.c4{left:4px;top:2438px;width:748px;height:484px;padding-top:56px}
.img-box{float:left;margin:0 40px 10px 0}
.justice{width:318px;height:318px;background:linear-gradient(160deg,#dfe3e4,#8c7a6a 55%,#c9cccd)}
.para-mark{width:240px;height:298px;margin:0 50px 10px 0;background:radial-gradient(ellipse at 45% 45%,#bdbdbd,#eeeeee 70%,#fff)}
.offices{display:flex;gap:0}
.offices div{width:338px}
.side{left:794px;top:853px;width:406px;height:2082px;border-radius:8px 0 0 8px;padding:0}
.side-head{text-align:center;font-size:35px;line-height:1.52;color:var(--dark);padding:34px 24px 0}
.side-head span{color:var(--red)}
.side h3{font-size:29px;color:var(--dark);margin:30px 0 22px 36px}
.benefits{list-style:none;margin:0 12px 0 36px}
.benefits li{border-bottom:1px dashed var(--rule);padding:8px 0 14px 20px;position:relative;color:#555}
.benefits li span{border-bottom:1px solid #bbb}
.benefits li::before{content:"";position:absolute;left:2px;top:20px;border-left:7px solid var(--red);border-top:5px solid transparent;border-bottom:5px solid transparent}
.benefits li:last-child{border-bottom:none}
.side-rule{border-top:1px solid var(--rule);margin-top:18px}
.side h4{font-weight:400;font-size:29px;color:var(--dark);margin:28px 0 18px 36px}
.services{margin:0 20px 0 36px}
.portrait{width:244px;height:320px;margin:60px 0 0 50px;border:4px solid #a8221b;background:linear-gradient(180deg,#c9871f,#9a4a17);border-radius:4px}
.side-rule2{border-top:1px solid var(--rule);margin-top:50px}
.notice{margin:54px 40px 0 82px;font-size:22px;line-height:1.2}
.side-links{margin:60px 0 0 82px;font-size:23px;line-height:2.05}
.banner{left:4px;top:3040px;width:1196px;height:58px;background:var(--red);color:#fff;text-align:center;font-size:37px;line-height:58px;letter-spacing:.5px}
.footer{left:0;top:3174px;width:1200px;text-align:center;font-size:23px;line-height:1.82}
.footer a{color:#333;text-decoration:underline}
.footer .copy{margin-top:24px;font-style:italic}
</style>
</head>
<body>
<p class="abs preheader">Dies ist der Kanzlei Morvenstein Newsletter vom 28.01.2012. Bitte fügen Sie email@kanzlei-morvenstein.de zu Ihrem Adressenverzeichnis hinzu, um sicherzustellen, dass Sie alle weiteren Mails von der Kanzlei Morvenstein erhalten.</p>

<div class="abs brand">
  <div class="brand-dot"></div>
  <div class="brand-name">Kanzlei Morvenstein<br>Rechtsanwälte</div>
</div>

<section class="abs hero">
  <div class="abs hero-visual" role="img" aria-label="Stapel silberner Paragraphenzeichen und ein großes rotes Paragraphenzeichen"></div>
  <p class="abs hero-tag">Zahlungsausfälle müssen nicht sein</p>
  <p class="abs hero-claim">Mahnwesen mit Anwalt für nur 99.- EUR jährlich</p>
  <div class="abs hero-strip">
    <svg width="36" height="36" viewBox="0 0 36 36"><circle cx="18" cy="18" r="16" fill="none" stroke="#fff" stroke-width="2.5"/><path d="M12 10c1-1 3-1 4 1l1 3c0 1-1 2-2 2 1 3 3 5 6 6 0-1 1-2 2-2l3 1c2 1 2 3 1 4-2 2-5 2-8 0-4-2-7-5-8-9-1-3-1-5 1-6z" fill="#fff"/></svg>
    <span>Kostenlose Info-Hotline 02236 - 4471290</span>
  </div>
  <div class="abs hero-side">
    <p class="hero-title">Mahnwesen mit<br>Anwalt - nur 99 EUR *<br>im Jahr</p>
    <p class="hero-sub"><b>Zahlungsausfälle müssen nicht sein</b> - kostenlose Info Hotline: 02236 - 4471290</p>
    <span class="cta">Jetzt Infos anfordern
      <svg width="32" height="22" viewBox="0 0 32 22"><path d="M2 2l9 9-9 9M14 2l9 9-9 9" fill="none" stroke="#fff" stroke-width="4"/></svg>
    </span>
  </div>
</section>

<section class="abs card c1">
  <h2>Sehr geehrter $Vorname$ $Nachname$</h2>
  <div class="img-box justice" role="img" aria-label="Bronzestatue der Justitia mit Waage"></div>
  <p>Hohe Außenstände und sogar Zahlungsausfälle bedrohen Ihre Kiquidität und bringen vielleicht auch Ihre Firma in Schwierigkeiten. Aber: Schlechte Zahlungsmoral kann bekämpft werden! Durch die frühzeitige Einschaltung eines Anwalts verbessert sich die erfahrungsgemäß die Zahlungsmoral Ihrer Gläubiger deutlich. <b>Optimieren auch Sie mit meiner Unterstützung Ihr Forderungsmanagment und sparen Sie gleichzeitig Zeit und Geld.</b></p>
</section>

<section class="abs card c2">
  <h2>Sie sparen bares Geld</h2>
  <div class="img-box para-mark" role="img" aria-label="Großes silbernes Paragraphenzeichen"></div>
  <p>Sie reduzieren Ihre Ausfallquote durch die rechtzeitige Einschaltung eines Rechtsanwalts. Gleichzeitig sparen Sie Geld für die Einschaltung eines Inkassounternehmens und haben von der zweiten Mahnung bis zur Zwangsvollstreckung nur einen einzigen Ansprechpartner. Schließlich gewinnen Sie wertvolle Zeit, die Sie für die Weiterentwicklung Ihres Geschäfts einsetzen können.</p>
</section>

<section class="abs card c3">
  <p>* Versand aller Mahnschreiben mit Anwaltsschreiben für die Dauer von 12 Monaten. Portokosten werden extra berechnet. Durchführung eines event. Vollstreckungsverfahren für die Mindestgebühren nach Rechtsanwaltvergütungsgesetz (RVG)</p>
</section>

<section class="abs card c4">
  <div class="offices">
    <div>Kanzlei Köln<br>Lindenhofweg 9<br>50999 Köln<br>koeln@kanzlei-morvenstein.de<br>Tel. 02236 - 4471290<br>Fax 02236 - 4471291</div>
    <div>Kanzlei Groß-Gerau<br>Mühlgasse 21<br>64521 Groß-Gerau<br>gross-gerau@kanzlei-<br>morvenstein.de<br>Tel. 06152 - 730411<br>Fax 06152 - 730412</div>
  </div>
</section>

<aside class="abs card side">
  <p class="side-head">Mahnwesen mit<br>Anwalt - <span>nur 99 EUR *<br>im Jahr</span></p>
  <h3>Ihre Vorteile im Überblick</h3>
  <ul class="benefits">
    <li><span>deutlich weniger Zahlungsausfälle durch frühzeitige Anwaltsschreiben</span></li>
    <li><span>Sie sparen Zeit und Nerven!</span></li>
    <li><span>keine zusätzlichen Inkassokosten</span></li>
    <li><span>unkomplizierte Abwicklung per E-Mail</span></li>
    <li><span>im Vollstreckungsverfahren zahlen Sie nur die gesetzlichen Mindesgebühren</span></li>
  </ul>
  <div class="side-rule"></div>
  <h4>Meine Leistungen für Sie</h4>
  <p class="services">Abwicklung aller Mahnschreiben bereits ab der zweiten Mahnstufe. Bei erfolglosen Mahnwesen werden auf Wunsch Mahn- und VOllstreckungsbescheide sowie die Vollstreckungshandlung (Kontopfändung oder Gerichtsvollzieher) erwirkt.</p>
  <div class="portrait" role="img" aria-label="Porträtfoto der Rechtsanwältin"></div>
  <div class="side-rule2"></div>
  <p class="notice">Sie erhalten den Newsletter weil Sie sich unter kanzlei-morvenstein.de für diesen Sercive angemeldet haben.</p>
  <p class="side-links">Meta<br>Impressum<br>Kontakt</p>
</aside>

<div class="abs banner">Jetzt kostenlos und unverbindlich anfragen</div>

<footer class="abs footer">
  <p>Die Berufsbezeichnung “Rechtsanwältin” wurde von der Bundesrepublik Deutschland verliehen.<br>Die einschlägigen berufsrechtlichen Regelungen (BRAO, BRAGO, BORA und RVG) finden Sie unter <a>www.kammerportal.de</a></p>
  <p style="margin-top:22px">Bitte klicken Sie <a>hier</a> wenn Sie diesen Newsletter in Zukunft nicht mehr erhalten möchten.</p>
  <p class="copy">Copyright © 2012 Kanzlei Morvenstein, <b>Alle Rechte vorbehalt</b>en</p>
</footer>
</body>
</html>
```